HPTW Morvane Terrace Bathroom Remodeling Postcard

We are a bathroom remodeling contractor in Los Angeles, California called Harbor Peak Tile Works. We want to create a postcard to send out to a specific condominium complex in the city of Burbank called Morvane Terrace. The postcard will be advertising a specific offer and should showcase our professionalism and quality of work. We have experience working in this particular housing development so we want to communicate that we are familiar with it. We want to be the first contractor that comes to mind when anyone who lives here starts thinking about a bathroom remodel in their home.

The postcard design should be an eye-catching combination of text and photos. The attached photos can be cropped if necessary. We have sent a variety of photos to choose from. Not all of the photos need to be included.

This is the specific text that should appear on the postcard:

Attn: Morvane Terrace Homeowners

2015 Bathroom Remodeling Sales Event!

Now through June 1, 2015 | Call Today for Details

Complete Custom Remodels Starting at $9999 (Labor and Materials)

14 days, Start to Finish, Fully-Permitted

Professional, Courteous, Quick & Clean!

harborpeaktileworks.example

Licensed (#452016), Bonded and Insured

818-555-0147

Morvane Terrace customer references available upon request. Some restrictions apply. Ad price for bathroom with tub/shower combo, call for price on shower only bathroom. Hard costs for permits not included. Tax on finish materials not included. Call today to lock in your special savings.

```html
<!DOCTYPE html>
<html lang="en">
<head>
<meta charset="utf-8">
<title>Harbor Peak Tile Works – Morvane Terrace Postcard</title>
<link href="https://fonts.googleapis.com/css2?family=Cinzel:wght@400;700&family=Roboto+Condensed:wght@300;400;500;700&family=Lato:wght@400;700&display=swap" rel="stylesheet">
<style>
  :root {
    --blue-light: #3a8fd0;
    --blue-mid: #1a5c9c;
    --blue-deep: #0a2b57;
    --navy-edge: #071c3d;
    --band-dark: #1b1e25;
    --band-darker: #121419;
    --white: #ffffff;
    --brand-blue: #9cc4ec;
    --tile-cream: #d9cbb4;
    --tile-stone: #b9a78c;
    --tile-grey: #c7cbcf;
    --tile-warm: #a8895f;
  }
  * { margin: 0; padding: 0; box-sizing: border-box; }
  html, body { width: 1200px; height: 947px; overflow: hidden; background: #ececec; }
  .postcard {
    position: relative;
    width: 1200px;
    height: 947px;
    overflow: hidden;
    color: var(--white);
    font-family: "Roboto Condensed", sans-serif;
  }
  .postcard__art { position: absolute; inset: 0; }
  .headline {
    position: absolute;
    left: 55px;
    top: 62px;
    font-family: "Cinzel", serif;
    font-weight: 700;
    font-size: 42px;
    line-height: 56px;
    letter-spacing: 1px;
    text-transform: uppercase;
  }
  .tagline {
    position: absolute;
    left: 55px;
    top: 248px;
    font-size: 22px;
    font-weight: 300;
    letter-spacing: 0.5px;
  }
  .event__year {
    position: absolute;
    left: 55px;
    top: 350px;
    font-size: 27px;
    font-weight: 400;
  }
  .event__title {
    position: absolute;
    left: 55px;
    top: 390px;
    font-size: 44px;
    font-weight: 400;
    letter-spacing: 5px;
  }
  .offer {
    position: absolute;
    left: 55px;
    top: 492px;
    font-size: 34px;
    font-weight: 500;
  }
  .offer__note {
    position: absolute;
    left: 55px;
    top: 545px;
    font-size: 29px;
    font-weight: 300;
  }
  .timeline {
    position: absolute;
    left: 55px;
    top: 622px;
    font-size: 26px;
    font-weight: 700;
  }
  .arc-text {
    font-family: "Roboto Condensed", sans-serif;
    font-size: 31px;
    font-weight: 400;
    letter-spacing: 5px;
    fill: var(--white);
  }
  .brand {
    position: absolute;
    left: 53px;
    top: 806px;
    display: flex;
    align-items: center;
    gap: 22px;
  }
  .brand__square {
    width: 100px;
    height: 100px;
    background: var(--blue-mid);
    border: 2px solid var(--white);
  }
  .brand__name {
    font-family: "Cinzel", serif;
    font-weight: 400;
    font-size: 30px;
    line-height: 38px;
    color: var(--brand-blue);
  }
  .contact {
    position: absolute;
    left: 750px;
    top: 766px;
    font-family: "Lato", sans-serif;
  }
  .contact__row { display: flex; align-items: center; gap: 10px; }
  .contact__phone { font-size: 34px; height: 44px; }
  .contact__web { font-size: 22px; margin-top: 20px; }
  .contact__license { font-size: 23px; margin-top: 22px; padding-left: 0; }
  .icon { flex: none; }
</style>
</head>
<body>
<main class="postcard">
  <svg class="postcard__art" width="1200" height="947" viewBox="0 0 1200 947" aria-hidden="false">
    <defs>
      <radialGradient id="bgBlue" cx="0.42" cy="0.45" r="0.75">
        <stop offset="0" stop-color="var(--blue-light)"/>
        <stop offset="0.45" stop-color="var(--blue-mid)"/>
        <stop offset="0.85" stop-color="var(--blue-deep)"/>
        <stop offset="1" stop-color="var(--navy-edge)"/>
      </radialGradient>
      <linearGradient id="bandDark" x1="0" y1="0" x2="0" y2="1">
        <stop offset="0" stop-color="var(--band-dark)"/>
        <stop offset="1" stop-color="var(--band-darker)"/>
      </linearGradient>
      <linearGradient id="photoShower" x1="0" y1="0" x2="1" y2="1">
        <stop offset="0" stop-color="#e6ddcc"/><stop offset="1" stop-color="var(--tile-stone)"/>
      </linearGradient>
      <linearGradient id="photoToilet" x1="0" y1="0" x2="1" y2="1">
        <stop offset="0" stop-color="#eef0f1"/><stop offset="1" stop-color="var(--tile-grey)"/>
      </linearGradient>
      <linearGradient id="photoGlass" x1="0" y1="0" x2="1" y2="1">
        <stop offset="0" stop-color="#d8c39c"/><stop offset="1" stop-color="var(--tile-warm)"/>
      </linearGradient>
      <linearGradient id="photoFixture" x1="0" y1="0" x2="1" y2="1">
        <stop offset="0" stop-color="#cdbb9f"/><stop offset="1" stop-color="#8e7a60"/>
      </linearGradient>
      <linearGradient id="photoTub" x1="0" y1="0" x2="1" y2="1">
        <stop offset="0" stop-color="#d3cbbd"/><stop offset="1" stop-color="#9a8f80"/>
      </linearGradient>
      <linearGradient id="photoWindow" x1="0" y1="0" x2="0" y2="1">
        <stop offset="0" stop-color="#c9b79a"/><stop offset="1" stop-color="#7d6a52"/>
      </linearGradient>
      <clipPath id="photoClip">
        <path d="M592 0 L1200 0 L1200 600 C1010 590 780 565 690 410 C640 320 612 170 592 0 Z"/>
      </clipPath>
    </defs>

    <rect class="backdrop" width="1200" height="947" fill="url(#bgBlue)"/>

    <g class="photo-grid" clip-path="url(#photoClip)">
      <rect x="586" y="0" width="614" height="600" fill="var(--white)"/>
      <rect x="596" y="4" width="139" height="284" fill="url(#photoShower)" role="img" aria-label="Photo of a tiled walk-in shower with a clerestory window"/>
      <rect x="739" y="4" width="231" height="284" fill="url(#photoToilet)" role="img" aria-label="Photo of a modern bathroom with a white toilet and dark vanity"/>
      <rect x="974" y="4" width="226" height="284" fill="url(#photoGlass)" role="img" aria-label="Photo of a frameless glass shower enclosure"/>
      <rect x="640" y="292" width="73" height="310" fill="url(#photoWindow)" role="img" aria-label="Photo of a bathroom window with shutters"/>
      <rect x="717" y="292" width="253" height="310" fill="url(#photoFixture)" role="img" aria-label="Photo of travertine shower wall with a chrome shower fixture"/>
      <rect x="974" y="292" width="226" height="310" fill="url(#photoTub)" role="img" aria-label="Photo of a tub and shower combo with glass sliding doors"/>
    </g>
    <path class="photo-grid__edge" d="M592 0 C612 170 640 320 690 410 C780 565 1010 590 1200 600" fill="none" stroke="var(--white)" stroke-width="8"/>

    <path class="contact-band" d="M0 800 C380 772 820 720 1200 668 L1200 947 L0 947 Z" fill="url(#bandDark)"/>
    <path class="contact-band__edge" d="M0 800 C380 772 820 720 1200 668" fill="none" stroke="var(--white)" stroke-width="7"/>

    <path id="deadlineArc" d="M118 770 C460 742 850 700 1180 648" fill="none"/>
    <text class="arc-text">
      <textPath href="#deadlineArc">Now through June 1, 2015   Call Today for Details</textPath>
    </text>
  </svg>

  <h1 class="headline">Morvane Terrace<br>Homeowners</h1>
  <p class="tagline">PROFESSIONAL, COURTEOUS, QUICK &amp; CLEAN!</p>
  <p class="event__year">2015 BATHROOM REMODELING</p>
  <p class="event__title">SALES EVENT!</p>
  <p class="offer">Complete Custom Remodels Starting at $9999</p>
  <p class="offer__note">(Labor and Materials)</p>
  <p class="timeline">14 days, Start to Finish, Fully-Permitted</p>

  <div class="brand">
    <div class="brand__square"></div>
    <p class="brand__name">Harbor Peak<br>Tile Works</p>
  </div>

  <div class="contact">
    <p class="contact__row contact__phone">
      <svg class="icon" width="32" height="32" viewBox="0 0 32 32" aria-hidden="true">
        <circle cx="16" cy="16" r="14" fill="none" stroke="var(--white)" stroke-width="2.5"/>
        <path d="M11 8 L14 12 L12.5 14 C13.5 16.5 15.5 18.5 18 19.5 L20 18 L24 21 L22 24 C15 24 8 17 8 10 Z" fill="var(--white)"/>
      </svg>
      818-555-0147
    </p>
    <p class="contact__row contact__web">
      <svg class="icon" width="22" height="22" viewBox="0 0 22 22" aria-hidden="true">
        <circle cx="11" cy="11" r="9.5" fill="none" stroke="var(--white)" stroke-width="1.8"/>
        <ellipse cx="11" cy="11" rx="4" ry="9.5" fill="none" stroke="var(--white)" stroke-width="1.5"/>
        <line x1="1.5" y1="11" x2="20.5" y2="11" stroke="var(--white)" stroke-width="1.5"/>
        <line x1="3" y1="6.5" x2="19" y2="6.5" stroke="var(--white)" stroke-width="1.2"/>
        <line x1="3" y1="15.5" x2="19" y2="15.5" stroke="var(--white)" stroke-width="1.2"/>
      </svg>
      www.harborpeaktileworks.example
    </p>
    <p class="contact__license">Licensed (#452016), Bonded and Insured</p>
  </div>
</main>
</body>
</html>
```